Maple & Lantern Flyer

2023 Maple & Lantern
Military, Veterans, Law Enforcement & Fire Fighters
Receive $300* Off Purchased Materials
*$300 maximum discount per order. $3,000 order minimum. Redeem up to 3 times per year.
Terms & Conditions: This program is intended for the professional contractor that supports Brindlecrest Supply with material purchases. One-time purchasers and institutions are not eligible for this program. By choosing to participate, you represent to Brindlecrest Supply that your participation is not prohibited by law. Brindlecrest Supply reserves the right to cancel, suspend, and/or modify this promotion at any time, for any reason, without prior notice. Employees at Brindlecrest Supply are not eligible to participate. All rights reserved by Brindlecrest Supply. Promotion expires December 31, 2023.
Please use our 2023 logo - attached
I'm also attaching the 2022 flyer as an example but looking for a refreshed design!

```html
<!DOCTYPE html>
<html lang="en">
<head>
<meta charset="utf-8">
<title>Maple &amp; Lantern Flyer</title>
<link href="https://fonts.googleapis.com/css2?family=Bebas+Neue&family=Montserrat:wght@600&family=Open+Sans:wght@400;600;800&display=swap" rel="stylesheet">
<style>
  :root {
    --page-bg: #e6e7ea;
    --blue-top: #1c5aa6;
    --blue-deep: #1d4b93;
    --blue-footer: #184589;
    --navy: #23307a;
    --white: #ffffff;
    --photo-military-a: #b7a58a;
    --photo-military-b: #6f7a8c;
    --photo-police-a: #c9c0ad;
    --photo-police-b: #2a2d36;
    --photo-fire-a: #b9cde0;
    --photo-fire-b: #a08b63;
  }
  * { margin: 0; padding: 0; box-sizing: border-box; }
  html, body { width: 1200px; height: 1044px; overflow: hidden; background: var(--page-bg); }
  .flyer {
    position: absolute; left: 213px; top: 22px;
    width: 773px; height: 1000px;
    color: var(--white);
    font-family: "Open Sans", sans-serif;
    box-shadow: 0 6px 24px rgba(0,0,0,.18);
    overflow: hidden;
  }
  .flyer-art { position: absolute; inset: 0; }
  .flyer-title {
    position: absolute; top: 62px; left: 0; right: 0; text-align: center;
    font-family: "Bebas Neue", sans-serif; font-size: 82px; line-height: 1; letter-spacing: 1px;
    text-shadow: 0 3px 6px rgba(0,0,0,.35);
  }
  .flyer-subtitle {
    position: absolute; top: 156px; left: 0; right: 0; text-align: center;
    font-weight: 800; font-size: 21px; letter-spacing: .3px; text-transform: uppercase;
  }
  .brand-seal {
    position: absolute; left: 520px; top: 478px; width: 170px; height: 170px;
    border-radius: 50%; background: var(--white);
    display: flex; align-items: center; justify-content: center; text-align: center;
    color: var(--navy); font-weight: 800; font-size: 19px; line-height: 1.2;
  }
  .offer { position: absolute; left: 62px; top: 588px; }
  .offer-receive { font-weight: 800; font-size: 26px; line-height: 1.3; text-transform: uppercase; letter-spacing: .5px; }
  .offer-amount {
    font-family: "Bebas Neue", sans-serif; font-size: 130px; line-height: .82; margin-top: 6px;
    text-shadow: 0 3px 6px rgba(0,0,0,.3);
  }
  .offer-amount .currency { font-size: 64px; vertical-align: 48px; margin-right: 2px; }
  .offer-amount .off { font-size: 68px; margin-left: 10px; }
  .offer-materials { font-weight: 800; font-size: 26px; line-height: 1.3; text-transform: uppercase; margin-top: 6px; letter-spacing: .3px; }
  .offer-fineprint {
    position: absolute; right: 40px; top: 672px; width: 300px;
    font-size: 11.5px; line-height: 1.4; text-align: right;
  }
  .terms {
    position: absolute; left: 62px; right: 44px; top: 798px;
    font-size: 9.5px; line-height: 1.45;
  }
  .social {
    position: absolute; right: 40px; top: 912px;
    display: flex; align-items: center; gap: 7px;
    font-family: "Montserrat", sans-serif; font-weight: 600; font-size: 15px;
  }
  .social-label { margin-right: 8px; }
  .social-square { width: 24px; height: 24px; border-radius: 4px; background: var(--white); opacity: .9; }
  .website {
    position: absolute; left: 62px; bottom: 16px;
    font-family: "Montserrat", sans-serif; font-weight: 600; font-size: 25px;
  }
</style>
</head>
<body>
<main class="flyer">
  <svg class="flyer-art" width="773" height="1000" viewBox="0 0 773 1000">
    <defs>
      <linearGradient id="grad-military" x1="0" y1="0" x2="1" y2="1">
        <stop offset="0" stop-color="var(--photo-military-a)"/><stop offset="1" stop-color="var(--photo-military-b)"/>
      </linearGradient>
      <linearGradient id="grad-police" x1="0" y1="0" x2="0" y2="1">
        <stop offset="0" stop-color="var(--photo-police-a)"/><stop offset="1" stop-color="var(--photo-police-b)"/>
      </linearGradient>
      <linearGradient id="grad-fire" x1="0" y1="0" x2="0" y2="1">
        <stop offset="0" stop-color="var(--photo-fire-a)"/><stop offset="1" stop-color="var(--photo-fire-b)"/>
      </linearGradient>
    </defs>
    <rect class="band-lower" width="773" height="1000" fill="var(--blue-deep)"/>
    <polygon class="band-top" points="0,0 773,0 773,210 440,262 330,300 0,345" fill="var(--blue-top)"/>
    <g role="img" aria-label="Photo of a smiling military family in front of a flag">
      <polygon points="0,345 230,314 230,510 0,565" fill="url(#grad-military)"/>
    </g>
    <g role="img" aria-label="Photo of two police officers in uniform">
      <polygon points="230,314 330,300 440,262 470,258 470,470 400,490 340,480 230,510" fill="url(#grad-police)"/>
    </g>
    <g role="img" aria-label="Photo of three firefighters in turnout gear beside a fire truck">
      <polygon points="470,258 773,210 773,392 470,470" fill="url(#grad-fire)"/>
    </g>
    <line x1="230" y1="314" x2="230" y2="510" stroke="var(--white)" stroke-width="4"/>
    <line x1="470" y1="258" x2="470" y2="470" stroke="var(--white)" stroke-width="4"/>
    <polyline points="0,345 330,300 440,262 773,210" fill="none" stroke="var(--white)" stroke-width="6"/>
    <polyline points="0,565 340,480 400,490 773,392" fill="none" stroke="var(--white)" stroke-width="6"/>
    <polygon class="band-footer" points="0,945 330,902 420,908 773,866 773,1000 0,1000" fill="var(--blue-footer)"/>
    <polyline points="0,945 330,902 420,908 773,866" fill="none" stroke="var(--white)" stroke-width="5"/>
  </svg>

  <h1 class="flyer-title">2023 Maple &amp; Lantern</h1>
  <p class="flyer-subtitle">Military, Veterans, Law Enforcement &amp; Fire Fighters</p>

  <div class="brand-seal">Brindlecrest<br>Supply</div>

  <section class="offer">
    <p class="offer-receive">Receive</p>
    <p class="offer-amount"><span class="currency">$</span>300<span class="off">Off</span></p>
    <p class="offer-materials">Purchased Materials</p>
  </section>

  <p class="offer-fineprint">*$300 maximum discount per order. $3,000 order minimum. Redeem up to 3 times per year.</p>

  <p class="terms">Terms &amp; Conditions: This program is intended for the professional contractor that supports Brindlecrest Supply with material purchases. One-time purchasers and institutions are not eligible for this program. By choosing to participate, you represent to Brindlecrest Supply that your participation is not prohibited by law. Brindlecrest Supply reserves the right to cancel, suspend, and/or modify this promotion at any time, for any reason, without prior notice. Employees at Brindlecrest Supply are not eligible to participate. All rights reserved by Brindlecrest Supply. Promotion expires December 31, 2023.</p>

  <div class="social">
    <span class="social-label">Follow Us @brindlecrestsupply</span>
    <span class="social-square"></span>
    <span class="social-square"></span>
    <span class="social-square"></span>
  </div>

  <p class="website">BrindlecrestSupply.com</p>
</main>
</body>
</html>
```